Quorvan Medical business cards

Double sided business cards.

Medical technology consulting company.

Business cards with two names on the front, upper to middle left:

Dr Colin R. Harbury BMed GAICD +61412558907
Dr Owen Palatsky PhD MCommrclLaw +61437619042

Email and website addresses bottom right:

colin@quorvanmedical.com.au
www.quorvanmedical.com.au

Tree logo (as per attached file) on front in a suitable position.

Tag line (as per attached files) on the back.

Need a file format to upload to Paper Haven or Cardlyner.

```html
<!DOCTYPE html>
<html lang="en">
<head>
<meta charset="utf-8">
<title>Quorvan Medical – Business Cards</title>
<link rel="stylesheet" href="https://fonts.googleapis.com/css2?family=Lato:wght@400&family=Open+Sans:wght@400;700&display=swap">
<style>
  :root {
    --bg: #d4d4d4;
    --card: #ffffff;
    --green: #4b8f3f;
    --maroon: #5c1212;
    --ink: #2b2b2b;
    --shadow: rgba(0, 0, 0, 0.28);
  }
  * { box-sizing: border-box; margin: 0; padding: 0; }
  html, body { width: 1200px; height: 896px; overflow: hidden; }
  body { background: var(--bg); position: relative; font-family: "Open Sans", sans-serif; }

  .card {
    position: absolute;
    left: 334px;
    width: 527px;
    height: 300px;
    background: var(--card);
    border-radius: 24px;
    box-shadow: 0 14px 22px var(--shadow);
  }
  .card--back { top: 126px; }
  .card--front { top: 474px; }

  .brand {
    position: absolute;
    display: flex;
    flex-direction: column;
    align-items: center;
    font-family: "Lato", sans-serif;
    font-weight: 400;
    color: var(--green);
    white-space: nowrap;
  }
  .brand__mark { border-radius: 50%; background: var(--green); flex: none; }

  .card--back .brand {
    left: 0; right: 0; top: 66px;
    font-size: 36px;
    line-height: 40px;
    letter-spacing: 0.3px;
  }
  .card--back .brand__mark { width: 96px; height: 96px; margin-bottom: 44px; }

  .tagline {
    position: absolute;
    left: 0; right: 0; top: 250px;
    text-align: center;
    font-family: "Lato", sans-serif;
    font-size: 25px;
    line-height: 30px;
    color: var(--green);
    white-space: nowrap;
  }
  .tagline__sep { font-size: 16px; color: var(--maroon); margin: 0 8px; vertical-align: 3px; }

  .contacts { position: absolute; left: 19px; top: 54px; color: var(--ink); }
  .person__name { font-weight: 700; font-size: 20px; line-height: 24px; color: var(--green); }
  .person__name b { color: var(--maroon); }
  .person__quals { font-size: 13.5px; line-height: 18px; }
  .line { display: flex; align-items: center; gap: 6px; font-size: 14.5px; line-height: 20px; }
  .line svg { width: 13px; height: 13px; flex: none; fill: var(--maroon); }
  .person + .person { margin-top: 8px; }
  .person .line { margin-top: 6px; }
  .web { margin-top: 8px; }

  .card--front .brand {
    left: 292px; width: 220px; top: 88px;
    font-size: 21.5px;
    line-height: 26px;
  }
  .card--front .brand__mark { width: 56px; height: 56px; margin-bottom: 28px; }
</style>
</head>
<body>

<section class="card card--back">
  <div class="brand"><span class="brand__mark"></span>QUORVAN MEDICAL</div>
  <p class="tagline">Concept<span class="tagline__sep">|</span>Commercialisation<span class="tagline__sep">|</span>Beyond</p>
</section>

<section class="card card--front">
  <div class="contacts">
    <div class="person">
      <p class="person__name">Dr Colin R. <b>Harbury</b></p>
      <p class="person__quals">BMed GAICD</p>
      <p class="line"><svg viewBox="0 0 24 24"><path d="M6.6 10.8a15.1 15.1 0 0 0 6.6 6.6l2.2-2.2a1 1 0 0 1 1-.25 11.4 11.4 0 0 0 3.6.57 1 1 0 0 1 1 1V20a1 1 0 0 1-1 1A17 17 0 0 1 3 4a1 1 0 0 1 1-1h3.5a1 1 0 0 1 1 1c0 1.25.2 2.45.57 3.570a1 1 0 0 1-.25 1z"/></svg>+61412558907</p>
    </div>
    <div class="person">
      <p class="person__name">Dr Owen <b>Palatsky</b></p>
      <p class="person__quals">PhD MCommrclLaw</p>
      <p class="line"><svg viewBox="0 0 24 24"><path d="M6.6 10.8a15.1 15.1 0 0 0 6.6 6.6l2.2-2.2a1 1 0 0 1 1-.25 11.4 11.4 0 0 0 3.6.57 1 1 0 0 1 1 1V20a1 1 0 0 1-1 1A17 17 0 0 1 3 4a1 1 0 0 1 1-1h3.5a1 1 0 0 1 1 1c0 1.25.2 2.45.57 3.57a1 1 0 0 1-.25 1z"/></svg>+61437619042</p>
    </div>
    <div class="web">
      <p class="line"><svg viewBox="0 0 24 24"><path d="M2 6h20v12H2zm2 2v.5l8 5 8-5V8l-8 5z"/></svg>colin@quorvanmedical.com.au</p>
      <p class="line"><svg viewBox="0 0 24 24"><path d="M12 2a10 10 0 1 0 0 20 10 10 0 0 0 0-20zm-1 17.9A8 8 0 0 1 4.2 10.5L9 15v1a2 2 0 0 0 2 2zm6.9-2.5A2 2 0 0 0 16 16h-1v-3a1 1 0 0 0-1-1H8v-2h2a1 1 0 0 0 1-1V7h2a2 2 0 0 0 2-2v-.4a8 8 0 0 1 2.9 12.8z"/></svg>www.quorvanmedical.com.au</p>
    </div>
  </div>
  <div class="brand"><span class="brand__mark"></span>QUORVAN MEDICAL</div>
</section>

</body>
</html>
```